nestliva - Ballon Design

I need a Ballon designed. Please use the psb file ballon_template.psb as template.

I would like to have a ballon designed similar to the file "example.png".
instead of the pellu tot logo please use my attached logo "nestliva logo.ai"

The text should be the same " IT'S A MOM" but the logo should be different.

I should look like more elegant. should be also white background. But for the design feel free.

thanks.

Please also add the webpage "www.nestliva.eu" on the ballon design.

```html
<!DOCTYPE html>
<html lang="en">
<head>
<meta charset="utf-8">
<title>nestliva – It's a mom balloon</title>
<link rel="stylesheet" href="https://fonts.googleapis.com/css2?family=Quicksand:wght@500;600&family=Archivo+Black&display=swap">
<style>
  :root {
    --paper: #ffffff;
    --outline: #555555;
    --rose: #cf7e9c;
    --navy: #4a6aa5;
    --navy-light: #8fa6d3;
    --mist: #e9eef2;
  }
  html, body {
    margin: 0;
    padding: 0;
    width: 935px;
    height: 1200px;
    overflow: hidden;
    background: var(--paper);
  }
  .balloon {
    display: block;
    width: 935px;
    height: 1200px;
  }
  .balloon-outline {
    fill: var(--paper);
    stroke: var(--outline);
    stroke-width: 2.5;
  }
  .ring {
    fill: none;
    stroke: url(#ringFade);
  }
  .ring--outer { stroke-width: 5; }
  .ring--inner { stroke-width: 2.5; }
  .heart { fill: var(--rose); }
  .headline {
    font-family: "Quicksand", sans-serif;
    font-weight: 600;
    font-size: 232px;
    fill: var(--rose);
    text-anchor: middle;
  }
  .web-address {
    font-family: "Archivo Black", sans-serif;
    font-size: 46px;
    fill: url(#urlFade);
  }
  .brand-name {
    font-family: "Quicksand", sans-serif;
    font-weight: 600;
    font-size: 66px;
    fill: var(--navy);
    text-anchor: middle;
  }
</style>
</head>
<body>
<svg class="balloon" viewBox="0 0 935 1200" xmlns="http://www.w3.org/2000/svg">
  <defs>
    <linearGradient id="ringFade" x1="0" y1="0" x2="1" y2="1">
      <stop offset="0" stop-color="var(--navy)"/>
      <stop offset="0.45" stop-color="var(--navy)"/>
      <stop offset="0.62" stop-color="var(--mist)"/>
      <stop offset="0.8" stop-color="var(--navy)"/>
      <stop offset="1" stop-color="var(--navy)"/>
    </linearGradient>
    <linearGradient id="urlFade" x1="0" y1="1" x2="1" y2="0">
      <stop offset="0" stop-color="var(--navy)"/>
      <stop offset="0.35" stop-color="var(--navy-light)"/>
      <stop offset="1" stop-color="var(--navy)"/>
    </linearGradient>
    <path id="heartShape" d="M0 12 C-4 6 -22 -2 -22 -16 C-22 -28 -8 -32 0 -20 C8 -32 22 -28 22 -16 C22 -2 4 6 0 12 Z"/>
    <path id="addressArc" d="M 76 424 A 400 400 0 0 1 556 100"/>
  </defs>

  <!-- balloon body and neck -->
  <path class="balloon-outline"
        d="M 409 931
           A 463 463 0 1 1 524 931
           C 520 990 522 1060 525 1110
           C 527 1140 495 1150 490 1165
           C 484 1182 443 1184 438 1165
           C 433 1148 410 1140 410 1110
           C 412 1060 414 990 409 931 Z"/>

  <!-- decorative ring -->
  <path class="ring ring--outer" d="M 605 100 A 414 414 0 1 1 54 484"/>
  <path class="ring ring--inner" d="M 600 110 A 404 404 0 1 1 64 486"/>

  <!-- web address along the top left -->
  <text class="web-address"><textPath href="#addressArc" textLength="585" lengthAdjust="spacing">www.nestliva.eu</textPath></text>

  <!-- hearts along the ring -->
  <use class="heart" href="#heartShape" transform="translate(615 96) rotate(28) scale(1.6)"/>
  <use class="heart" href="#heartShape" transform="translate(850 392) rotate(-8) scale(1.7)"/>
  <use class="heart" href="#heartShape" transform="translate(784 680) rotate(-40) scale(1.7)"/>
  <use class="heart" href="#heartShape" transform="translate(500 889) rotate(-90) scale(1.1)"/>
  <use class="heart" href="#heartShape" transform="translate(205 783) rotate(-130) scale(1.1)"/>
  <use class="heart" href="#heartShape" transform="translate(92 557) rotate(-100) scale(0.95)"/>
  <use class="heart" href="#heartShape" transform="translate(64 478) rotate(0) scale(0.95)"/>

  <!-- headline -->
  <text class="headline" x="458" y="341">It’s</text>
  <text class="headline" x="455" y="502">a</text>
  <text class="headline" x="455" y="652">mom</text>

  <!-- brand name -->
  <text class="brand-name" x="469" y="784">nestliva</text>
</svg>
</body>
</html>
```